Our New Website is Now Live!

New website launch, with ability to place orders and save quotes online. Our previous website was resource oriented – www.quellvalvekits.com – and new website will be up to date, more interactive, more modern and have all and more repair resources. Company colors are in logo below and throughout new website – https://staging.tidegatefixers.com/. We have always offered free technical phone support and we now will have the ability to chat live on the website with our team for customer service, technical support and any issues.

Target Market(s)

blue collar, 40-60 year old blue collar workers. Message needs to be clear and most people that will see this flyer are not familiar with our old website

Requirements
Must have
• new website launch, repair help, technical assistance
Nice to have
• online chat, pictures from website of product

```html
<!DOCTYPE html>
<html lang="en">
<head>
<meta charset="UTF-8">
<title>Our New Website is Now Live!</title>
<link href="https://fonts.googleapis.com/css2?family=Lato:wght@400;700;900&display=swap" rel="stylesheet">
<style>
  :root {
    --blue: #3c4f9b;
    --blue-dark: #2f3f84;
    --red: #e1284b;
    --white: #ffffff;
    --ink: #2c2f3a;
    --photo-a: #9a9893;
    --photo-b: #c9a867;
  }
  * { box-sizing: border-box; margin: 0; padding: 0; }
  html, body { width: 850px; height: 1200px; overflow: hidden; background: var(--white); }
  body { font-family: 'Lato', sans-serif; color: var(--white); }
  .flyer { position: relative; width: 850px; height: 1200px; overflow: hidden; background: var(--white); }

  .hero-shapes { position: absolute; left: 0; top: 0; width: 850px; height: 586px; }

  .brand-top {
    position: absolute; left: 50px; top: 80px;
    display: flex; align-items: center; gap: 14px;
    color: var(--blue); font-weight: 900; font-size: 30px; line-height: 1.05;
  }
  .brand-top .mark { width: 30px; height: 30px; background: var(--red); flex: none; }

  .headline { position: absolute; left: 52px; top: 300px; line-height: 1.08; }
  .headline .line-light { display: block; font-size: 52px; font-weight: 400; }
  .headline .line-bold { display: block; font-size: 80px; font-weight: 900; letter-spacing: 0.5px; }

  .url-pill {
    position: absolute; left: 44px; top: 518px; width: 386px; height: 36px;
    background: var(--white); border-radius: 18px;
    color: var(--blue); font-weight: 700; font-size: 17px;
    display: flex; align-items: center; justify-content: center;
  }

  .services {
    position: absolute; left: 0; top: 586px; width: 850px; height: 292px;
    background: var(--red); display: flex; padding: 36px 30px 0;
  }
  .service { flex: 1; text-align: center; padding: 0 18px; position: relative; }
  .service + .service::before {
    content: ""; position: absolute; left: 0; top: 78px; width: 3px; height: 150px; background: var(--white);
  }
  .service svg { width: 52px; height: 52px; display: block; margin: 0 auto 14px; }
  .service h2 { font-size: 31px; font-weight: 700; line-height: 1.05; }
  .service p { font-size: 15.5px; line-height: 1.3; margin-top: 2px; }

  .products {
    position: absolute; left: 60px; top: 896px; width: 730px;
    display: grid; grid-template-columns: repeat(6, 1fr); gap: 14px 22px;
  }
  .product { height: 86px; border-radius: 6px; }
  .p-grey { background: linear-gradient(160deg, #eceae6, #b9b6b0); }
  .p-red { background: linear-gradient(160deg, #e07a55, #a83a22); }
  .p-brass { background: linear-gradient(160deg, #e6c98c, #a77a33); }
  .p-green { background: linear-gradient(160deg, #6fa37d, #2e6a45); }
  .p-steel { background: linear-gradient(160deg, #d9dbe0, #7d8089); }

  .footer-bar { position: absolute; left: 0; top: 1098px; width: 850px; height: 102px; }
  .footer-brand {
    position: absolute; left: 48px; top: 1128px;
    display: flex; align-items: center; gap: 12px;
    color: var(--blue); font-weight: 400; line-height: 1.05;
  }
  .footer-brand .mark { width: 24px; height: 24px; background: var(--red); flex: none; }
  .footer-brand .name { font-size: 26px; display: block; }
  .footer-brand .sub { font-size: 15px; display: block; margin-top: 2px; }
  .footer-url {
    position: absolute; right: 40px; top: 1137px;
    font-size: 18px; font-weight: 700; color: var(--white);
  }
</style>
</head>
<body>
<main class="flyer">
  <svg class="hero-shapes" viewBox="0 0 850 586">
    <defs>
      <linearGradient id="photoTone" x1="0" y1="0" x2="1" y2="1">
        <stop offset="0" stop-color="#9a9893"/>
        <stop offset="1" stop-color="#c9a867"/>
      </linearGradient>
    </defs>
    <polygon points="522,0 850,0 850,586 430,586" fill="url(#photoTone)" role="img" aria-label="Photo of backflow valve repair parts, brass fittings and a wrench on concrete"/>
    <polygon points="455,0 522,0 430,586 0,586 0,227 419,227" fill="var(--blue)"/>
    <polygon points="405,0 446,0 411,227 370,227" fill="var(--red)"/>
  </svg>

  <div class="brand-top"><span class="mark"></span><span>Tidegate Valve<br>Supply</span></div>

  <h1 class="headline">
    <span class="line-light">Our New</span>
    <span class="line-bold">Website</span>
    <span class="line-light">is Now Live!</span>
  </h1>
  <div class="url-pill">www.staging.tidegatefixers.com</div>

  <section class="services">
    <div class="service">
      <svg viewBox="0 0 52 52"><path d="M8 8h36a4 4 0 0 1 4 4v20a4 4 0 0 1-4 4H22l-10 9v-9H8a4 4 0 0 1-4-4V12a4 4 0 0 1 4-4z" fill="var(--white)"/><circle cx="16" cy="22" r="3.2" fill="var(--red)"/><circle cx="26" cy="22" r="3.2" fill="var(--red)"/><circle cx="36" cy="22" r="3.2" fill="var(--red)"/></svg>
      <h2>Chat Live!</h2>
      <p>on the website with our team for customer service, technical support and any issues.</p>
    </div>
    <div class="service">
      <svg viewBox="0 0 52 52"><path d="M26 4l4 5 6-2 1 6 6 2-2 6 5 5-5 4 2 6-6 2-1 6-6-2-4 5-4-5-6 2-1-6-6-2 2-6-5-4 5-5-2-6 6-2 1-6 6 2z" fill="var(--white)"/><path d="M18 34l10-10M28 24a5 5 0 1 0 6-6l-3 3-3-1-1-3 3-3" stroke="var(--red)" stroke-width="3" fill="none" stroke-linecap="round"/></svg>
      <h2>Repair Help</h2>
      <p>Get access to helpful parts breakdowns, repair procedures, videos, and spec sheets.</p>
    </div>
    <div class="service">
      <svg viewBox="0 0 52 52"><path d="M10 42l20-20M34 8a8 8 0 0 0-8 10l-18 18 6 6 18-18a8 8 0 0 0 10-8l-5 5-5-1-1-5z" fill="var(--white)" stroke="var(--white)" stroke-width="3" stroke-linejoin="round"/><path d="M12 10l14 14M10 12l4-4 4 4-4 4zM30 30l10 10" stroke="var(--white)" stroke-width="5" stroke-linecap="round"/></svg>
      <h2>Technical<br>Assistance</h2>
      <p>Free Phone Tech Assistance<br>Live Chat Tech Assistance<br>Experienced Technicians On Staff, Step-By-Step Repair Instructions, Repair Videos</p>
    </div>
  </section>

  <section class="products">
    <div class="product p-grey" role="img" aria-label="Product photo: insulated valve enclosure"></div>
    <div class="product p-red" role="img" aria-label="Product photo: gate valve"></div>
    <div class="product p-brass" role="img" aria-label="Product photo: brass check valve"></div>
    <div class="product p-brass" role="img" aria-label="Product photo: brass test cocks"></div>
    <div class="product p-brass" role="img" aria-label="Product photo: brass flare fitting"></div>
    <div class="product p-brass" role="img" aria-label="Product photo: ball valve with actuator"></div>
    <div class="product p-red" role="img" aria-label="Product photo: rubber flange gasket"></div>
    <div class="product p-red" role="img" aria-label="Product photo: resilient seat gate valve"></div>
    <div class="product p-steel" role="img" aria-label="Product photo: valve test kit hose"></div>
    <div class="product p-green" role="img" aria-label="Product photo: green backflow cage"></div>
    <div class="product p-steel" role="img" aria-label="Product photo: combination padlock"></div>
    <div class="product p-steel" role="img" aria-label="Product photo: stainless mounting hardware"></div>
  </section>

  <svg class="footer-bar" viewBox="0 0 850 102" aria-hidden="true">
    <polygon points="388,0 425,0 408,102 371,102" fill="var(--red)"/>
    <polygon points="432,0 850,0 850,102 415,102" fill="var(--blue)"/>
  </svg>
  <div class="footer-brand"><span class="mark"></span><span><span class="name">Tidegate Valve</span><span class="sub">Supply Company</span></span></div>
  <div class="footer-url">www.staging.tidegatefixers.com</div>
</main>
</body>
</html>
```